vQ CARELINE (Brochure Design)

i need a proffesional brochure made. we are a mobile medical service company providing mobile Arterial Blood Gases(ABG's). Respiratory & Ventilator Consultation services. Ventilator and Tracheostomy training courses. and mobile vaccine administration.

this is my first time making a brochure so any and all advice/guidance will be appreciated.

i am thinking prints will be 8.5 inches x 11 inches (TRI-FOLD and BI-FOLD)

i have uploaded my business card design and logo design for reference.
as this brochure project continues ill update needs of the project descriptions.

Introduction: At vq CARELINE, we're dedicated to enhancing healthcare services by providing exceptional mobile arterial blood gases, respiratory and ventilator consultation services. Our core values revolve around excellence, compassion and accessibility. We believe that every individual deserves the highest standard of care, and we're committed to delivering that through expert guidance and top-notch training courses. Your health is at the heart of what we do, and we're here to support you on your journey to better respiratory health.

Mobile Arterial Blood Gases : Our mobile Arterial Blood Gas service offers quick, on-the-spot analysis of pH, oxygen, and carbon dioxide levels in your the blood. This service enables rapid adjustments to treatment plans for more effective respiratory care.

Ventilator and Tracheostomy Training: Our ventilator and tracheostomy course empowers caregivers and healthcare professionals to manage ventilators and care for tracheostomy patients with expertise. This training enhances patient safety, treatment outcomes, and healthcare provider confidence. vQ Careline your choice for top-notch care, convenience, and peace of mind.

Respiratory Consulting: Our respiratory consulting services provide expert guidance and support for individuals with respiratory / ventilator concerns. Benefits include personalized treatment plans, better management of respiratory conditions, and improved overall lung health. vQ Careline is your trusted partner for a breath of fresh air.

Target Market(s)

Sub-Acute facilities, Pulmonary Clinics, Pulmonologists, Nurses, Caregivers, Hospice and homehealth companies.

Industry/Entity Type

Medical; Respiratory; Nursing

Requirements
Must have
• proffesional simple design.

```html
<!DOCTYPE html>
<html lang="en">
<head>
<meta charset="utf-8">
<title>vQ Careline Tri-fold Brochure</title>
<link href="https://fonts.googleapis.com/css2?family=Montserrat:wght@400;500;600;700&family=Roboto+Condensed:wght@400;500&display=swap" rel="stylesheet">
<style>
:root{
  --blue:#1565c0;
  --blue-deep:#0d4fa8;
  --green:#1fa84a;
  --green-bright:#22b14c;
  --ink:#1e2a38;
  --bg:#e9ecef;
  --white:#ffffff;
}
*{box-sizing:border-box;margin:0;padding:0}
html,body{width:1137px;height:1200px;overflow:hidden;background:var(--bg);font-family:"Montserrat",sans-serif;color:var(--ink)}
.spread{position:absolute;left:183px;width:771px;height:560px;display:flex;box-shadow:0 8px 24px rgba(0,0,0,.18)}
.spread--outside{top:25px}
.spread--inside{top:615px}
.panel{position:relative;width:257px;height:560px;overflow:hidden}
.panel--light{background:linear-gradient(135deg,#e4e7ea 0%,#f7f8f9 55%,#ffffff 100%)}
.panel--gradient{background:linear-gradient(180deg,var(--green-bright) 0%,#129a73 45%,var(--blue) 100%);color:var(--white)}
.panel--green{background:var(--green-bright);color:var(--white)}
.panel--cover{background:var(--white)}
.abs{position:absolute}
.photo{position:absolute}
.heading{position:absolute;font-weight:700;font-size:11.5px;line-height:1.15;color:var(--blue);padding:3px 6px;border-left:1px solid var(--green);border-top:1px solid var(--green)}
.heading::after{content:"";position:absolute;right:-1px;top:-1px;width:1px;height:60%;background:var(--green)}
.body{position:absolute;font-size:9.6px;line-height:1.45}
.body p+p{margin-top:9px}
.brand{position:absolute;left:0;width:257px;display:flex;justify-content:center;align-items:center;gap:8px;font-weight:700;font-size:16px;letter-spacing:.3px}
.brand-mark{display:inline-block;width:12px;height:12px;border-radius:50%}
.brand--cover{color:var(--ink)}
.brand--contact{color:var(--white)}
.abg-title{position:absolute;left:-8px;width:257px;text-align:center;font-family:"Roboto Condensed",sans-serif;font-weight:500;font-size:11.5px}
.abg-table{position:absolute;left:17px;top:322px;width:134px;border-collapse:collapse;font-family:"Roboto Condensed",sans-serif;font-size:9.5px;background:var(--white);border:1px solid #333}
.abg-table th,.abg-table td{border-bottom:1px solid #333;padding:3px 3px;text-align:center;font-weight:400}
.abg-table th{font-weight:500}
.abg-table sub{font-size:6px}
.contact{position:absolute;left:0;width:257px;text-align:center;font-size:11.5px;letter-spacing:.4px}
.contact svg{display:block;margin:0 auto 8px}
.cover-title{position:absolute;left:0;width:257px;text-align:center;font-weight:600;font-size:18px;line-height:1.35}
.cover-band{position:absolute;left:0;top:359px;width:257px;height:201px;background:var(--blue-deep);color:var(--white)}
.cover-line{position:absolute;left:23px;font-weight:600;font-size:12.5px;line-height:1.3}
.url-btn{position:absolute;left:14px;top:149px;background:var(--green-bright);color:var(--white);font-weight:600;font-size:11px;padding:4px 8px}
.service{position:absolute;left:14px;width:100px;text-align:center;font-size:9.5px;line-height:1.1}
.service svg{display:block;margin:0 auto 4px}
.blue-block{position:absolute;left:0;top:274px;width:257px;height:286px;background:var(--blue-deep);color:var(--white)}
.blue-block .heading{color:var(--green-bright);border-color:var(--green-bright)}
.blue-block .heading::after{background:var(--green-bright)}
</style>
</head>
<body>

<section class="spread spread--outside">
  <div class="panel panel--light">
    <h2 class="heading" style="left:13px;top:50px">RESPIRATORY<br>CONSULTING:</h2>
    <div class="body" style="left:15px;top:92px;width:222px">
      <p>Our respiratory consulting services provide expert guidance and support for individuals with respiratory / ventilator concerns.</p>
      <p>Benefits include personalized treatment plans, better management of respiratory conditions, and improved overall lung health.</p>
      <p>vQ Careline is your trusted partner for a breath of fresh air.</p>
    </div>
    <div class="abg-title" style="top:288px">Arterial Blood Gas (ABG)</div>
    <table class="abg-table">
      <tr><th>ABG</th><th>Normal range</th></tr>
      <tr><td>O<sub>2</sub>CT</td><td>15-23% per 100 mL of blood</td></tr>
      <tr><td>pH</td><td>7.35-7.45</td></tr>
      <tr><td>PaCO<sub>2</sub></td><td>35-45 mmHg</td></tr>
      <tr><td>PaO<sub>2</sub></td><td>80-100 mmHg</td></tr>
      <tr><td>HCO<sub>3</sub></td><td>22-26 mEq/L</td></tr>
      <tr><td>O<sub>2</sub>Sat</td><td>95-100%</td></tr>
    </table>
    <div class="photo" role="img" aria-label="Medical illustration of a forearm with the radial artery and a syringe drawing arterial blood" style="left:158px;top:320px;width:88px;height:225px;background:linear-gradient(180deg,#c76a58,#9c5446 60%,#b87c66);border-radius:40px 40px 30px 30px;opacity:.85"></div>
  </div>

  <div class="panel panel--gradient">
    <div class="brand brand--contact" style="top:160px">
      <span class="brand-mark" style="background:var(--white)"></span>vQ Careline
    </div>
    <div class="contact" style="top:216px">
      <svg width="10" height="10" viewBox="0 0 24 24" fill="#fff"><path d="M6.6 10.8a15.1 15.1 0 0 0 6.6 6.6l2.2-2.2c.3-.3.7-.4 1-.2 1.1.4 2.3.6 3.6.6.6 0 1 .4 1 1V20c0 .6-.4 1-1 1A17 17 0 0 1 3 4c0-.6.4-1 1-1h3.5c.6 0 1 .4 1 1 0 1.3.2 2.5.6 3.6.1.3 0 .7-.2 1z"/></svg>
      555.014.2290
    </div>
    <div class="contact" style="top:268px">
      <svg width="10" height="8" viewBox="0 0 24 18" fill="#fff"><path d="M0 0h24v3l-12 7L0 3z"/><path d="M0 6l12 7 12-7v12H0z"/></svg>
      info@vqcarelinegroup.com
    </div>
    <div class="contact" style="top:318px">
      <svg width="10" height="10" viewBox="0 0 24 24" fill="#fff"><rect x="6" y="1" width="12" height="7"/><rect x="2" y="9" width="20" height="14" rx="2"/></svg>
      555.014.7781
    </div>
    <div class="contact" style="top:372px">
      <svg width="11" height="11" viewBox="0 0 24 24" fill="none" stroke="#fff" stroke-width="2"><circle cx="12" cy="12" r="10"/><path d="M2 12h20M12 2c3 3 3 17 0 20M12 2c-3 3-3 17 0 20"/></svg>
      vqcarelinegroup.com
    </div>
  </div>

  <div class="panel panel--cover">
    <div class="photo" role="img" aria-label="Photo of a patient with a tracheostomy resting in a hospital bed beside a ventilator, with a nurse attending" style="left:0;top:80px;width:257px;height:279px;background:linear-gradient(180deg,#ffffff 0%,#e6edf4 25%,#b9c9dc 60%,#8aa6c8 100%)"></div>
    <div class="brand brand--cover" style="top:40px">
      <span class="brand-mark" style="background:var(--green-bright)"></span>vQ Careline
    </div>
    <div class="cover-title" style="top:96px">
      <span style="color:var(--blue)">Mobile Arterial</span><br>
      <span style="color:var(--green)">Blood Gases(ABG's).</span>
    </div>
    <div class="cover-band">
      <div class="cover-line" style="top:28px">Respiratory &amp; Ventilator<br>Consultation services.</div>
      <div class="cover-line" style="top:82px">Ventilator and Tracheostomy<br>training courses and mobile<br>vaccine administration.</div>
      <div class="url-btn">www.vqcarelinegroup.com</div>
    </div>
  </div>
</section>

<section class="spread spread--inside">
  <div class="panel panel--light">
    <div class="photo" role="img" aria-label="Close-up photo of gloved hands drawing an arterial blood sample from a wrist" style="left:26px;top:25px;width:204px;height:107px;background:linear-gradient(135deg,#5c6f8f,#c9ccd4 55%,#9fb7c4);border:1px solid var(--blue)"></div>
    <h2 class="heading" style="left:23px;top:160px">INTRODUCTION:</h2>
    <div class="body" style="left:23px;top:196px;width:215px">
      <p>At vq CARELINE, we're dedicated to enhancing healthcare services by providing exceptional mobile arterial blood gases, respiratory and ventilator consultation services. Our core values revolve around excellence, compassion and accessibility.</p>
      <p>We believe that every individual deserves the highest standard of care, and we're committed to delivering that through expert guidance and top-notch training courses. Your health is at the heart of what we do, and we're here to support you on your journey to better respiratory health.</p>
    </div>
    <div class="photo" role="img" aria-label="Product photo of two portable ventilators" style="left:30px;top:416px;width:200px;height:120px;background:linear-gradient(160deg,#dfe7f2,#9db4d6 60%,#e9eef5);border-radius:8px"></div>
  </div>

  <div class="panel panel--green">
    <h2 class="abs" style="left:21px;top:26px;font-size:11.5px;font-weight:700;line-height:1.25">MOBILE ARTERIAL BLOOD<br>GASES :</h2>
    <div class="body" style="left:21px;top:70px;width:222px;font-size:9.3px;line-height:1.6">
      <p>Our mobile Arterial Blood Gas service offers quick, on-the-spot analysis of pH, oxygen, and carbon dioxide levels in the blood. This service enables rapid adjustments to treatment plans for more effective respiratory care.</p>
    </div>
    <div class="service" style="top:170px">
      <svg width="30" height="30" viewBox="0 0 30 30"><circle cx="15" cy="15" r="14" fill="none" stroke="#fff" stroke-width="1.4"/><path d="M15 8v7M15 13l-4 2v6h-2v-7zM15 13l4 2v6h2v-7z" fill="#fff" stroke="#fff"/></svg>
      Respiratory<br>Consultations
    </div>
    <div class="service" style="top:248px">
      <svg width="30" height="30" viewBox="0 0 30 30"><circle cx="15" cy="15" r="14" fill="none" stroke="#fff" stroke-width="1.4"/><path d="M9 21l9-9M16 10l4 4M20 8l2 2" stroke="#fff" stroke-width="2.4" fill="none"/></svg>
      In-house<br>ABG's
    </div>
    <div class="service" style="top:324px">
      <svg width="30" height="30" viewBox="0 0 30 30"><circle cx="15" cy="15" r="14" fill="none" stroke="#fff" stroke-width="1.4"/><rect x="10" y="9" width="10" height="9" fill="none" stroke="#fff" stroke-width="1.6"/><path d="M12 18v4h6v-4" stroke="#fff" stroke-width="1.6" fill="none"/></svg>
      Ventilator<br>Training
    </div>
    <div class="photo" role="img" aria-label="Product photo of a portable ventilator with a control panel" style="left:120px;top:228px;width:118px;height:164px;background:linear-gradient(180deg,#4b3f8f 0%,#eceef2 12%,#d4d8df 75%,#4b3f8f 100%);border-radius:6px"></div>
    <div class="photo" role="img" aria-label="Green-tinted photo of a clinician working with respiratory equipment" style="left:0;top:410px;width:257px;height:150px;background:linear-gradient(180deg,var(--green-bright),#0f6b2f 60%,#0b4f23)"></div>
  </div>

  <div class="panel" style="background:var(--white)">
    <div class="photo" role="img" aria-label="Photo of blue-gloved hands taking a blood sample from an arm" style="left:0;top:0;width:257px;height:134px;background:linear-gradient(135deg,#3a3f4a,#c9b3a3 55%,#3f6fcf)"></div>
    <div class="photo" role="img" aria-label="Photo of an arterial blood draw from a wrist" style="left:0;top:138px;width:257px;height:136px;background:linear-gradient(135deg,#5d6e8c,#d1cbc6 55%,#a9c1cc)"></div>
    <div class="blue-block">
      <h2 class="heading" style="left:18px;top:18px">VENTILATOR AND<br>TRACHEOSTOMY TRAINING:</h2>
      <div class="body" style="left:23px;top:70px;width:190px;font-size:9.2px">
        <p>Our ventilator and tracheostomy course empowers caregivers and healthcare professionals to manage ventilators and care for tracheostomy patients with expertise.</p>
      </div>
      <div class="photo" role="img" aria-label="Product photo of a portable ventilator" style="left:10px;top:158px;width:82px;height:95px;background:linear-gradient(160deg,#b9c8e0,#7f98c2);border-radius:6px"></div>
      <div class="body" style="left:98px;top:154px;width:150px;font-size:9.2px">
        <p>This training enhances patient safety, treatment outcomes, and healthcare provider confidence. vQ Careline your choice for top-notch care, convenience, and peace of mind.</p>
      </div>
    </div>
  </div>
</section>

</body>
</html>
```